Solmira Full Spectrum CBD Oil infused with turmeric, black pepper and cacao extracts

Using company logo attached, dosage info attached, NHC disclaimer attached, pharmacist disclaimer below, ingredient list below and bar code.
Above "Full Spectrum" part of the logo I would like "Solmira" in hand written font and in light green color close to the logo color. White background color please. The smaller logos that were attached in the file need to be on the back side of the label with the ingridients list to the right of the logo in and the disclaimers to the left of it.

Requirements
Must have
• -ORGANIC
• -USA GROWN
• -30mL
• -1500MG CBD
• -This product is not approved by NHC for the diagnosis, cure, mitigation, treatment, or prevention of any disease. Please consult with your physician or pharmacist before using CBD if you are taking medication of any kind.
• -Directions: Administer 5 drops sublingually 2-3 times per day or as needed. Hold under your tongue for 60 seconds then swallow.
• -Ingredients: Organic MCT Oil, Organic Hemp Extract, proprietary organic terpene blend, Organic Hemp derived minerals

```html
<!DOCTYPE html>
<html lang="en">
<head>
<meta charset="UTF-8">
<title>Solmira Full Spectrum CBD Oil – Front Label</title>
<link rel="stylesheet" href="https://fonts.googleapis.com/css2?family=Montserrat:wght@500;600;700&family=Oswald:wght@600;700&family=Libre+Baskerville&display=swap">
<style>
  :root {
    --page-bg: #ffffff;
    --label-bg: #ececed;
    --brand-green: #1f5a1c;
    --leaf-green: #3f7d2a;
    --band-green: #2e6a1e;
    --ink: #141414;
    --band-text: #d3dfcb;
    --band-rule: rgba(255, 255, 255, 0.18);
  }
  * { box-sizing: border-box; margin: 0; padding: 0; }
  html, body {
    width: 1200px;
    height: 900px;
    overflow: hidden;
    background: var(--page-bg);
  }
  .canvas {
    position: relative;
    width: 1200px;
    height: 900px;
  }
  .front-label {
    position: absolute;
    left: 340px;
    top: 70px;
    width: 520px;
    height: 760px;
    background: var(--label-bg);
    font-family: "Montserrat", sans-serif;
    color: var(--ink);
    text-align: center;
  }
  .label-line {
    position: absolute;
    left: 0;
    width: 100%;
    transform: translateY(-50%);
    white-space: nowrap;
  }
  .brand-name {
    top: 106px;
    font-weight: 600;
    font-size: 40px;
    color: var(--leaf-green);
  }
  .product-line {
    top: 170px;
    font-weight: 500;
    font-size: 38px;
    letter-spacing: -0.5px;
  }
  .brand-dot {
    position: absolute;
    left: 205px;
    top: 227px;
    width: 110px;
    height: 110px;
  }
  .tagline {
    top: 400px;
    font-weight: 500;
    font-size: 38px;
    letter-spacing: -0.5px;
  }
  .product-title {
    top: 513px;
    font-family: "Oswald", sans-serif;
    font-weight: 700;
    font-size: 122px;
    line-height: 1;
    letter-spacing: 1px;
  }
  .product-title .cbd { color: var(--brand-green); }
  .product-title .oil { color: var(--ink); }
  .subtitle {
    top: 604px;
    font-weight: 500;
    font-size: 26px;
    letter-spacing: -0.3px;
  }
  .spec-band {
    position: absolute;
    left: 0;
    bottom: 0;
    width: 100%;
    height: 132px;
    background: var(--band-green);
    display: flex;
    align-items: center;
    justify-content: center;
    color: var(--band-text);
  }
  .spec-item {
    height: 100%;
    display: flex;
    align-items: center;
    justify-content: center;
    padding: 0 18px;
  }
  .spec-item + .spec-item { border-left: 1px solid var(--band-rule); }
  .spec-origin, .spec-volume {
    font-family: "Libre Baskerville", serif;
    font-size: 25px;
    line-height: 1.15;
  }
  .spec-origin { text-align: right; }
  .spec-volume { text-align: left; }
  .spec-strength {
    font-family: "Montserrat", sans-serif;
    font-weight: 700;
    font-size: 44px;
    letter-spacing: 0.5px;
  }
  .spec-strength small {
    font-size: 16px;
    margin-left: 5px;
  }
</style>
</head>
<body>
  <main class="canvas">
    <section class="front-label">
      <div class="label-line brand-name">Solmira</div>
      <div class="label-line product-line">FULL SPECTRUM</div>
      <svg class="brand-dot" viewBox="0 0 110 110" aria-hidden="true">
        <circle cx="55" cy="55" r="50" fill="var(--brand-green)"/>
      </svg>
      <div class="label-line tagline">HOLISTIC HEALING</div>
      <h1 class="label-line product-title"><span class="cbd">CBD</span> <span class="oil">OIL</span></h1>
      <div class="label-line subtitle">Nutrient Rich Dietary Supplement</div>
      <div class="spec-band">
        <div class="spec-item spec-origin">Organic<br>USA<br>Grown</div>
        <div class="spec-item spec-strength">1500<small>MG</small></div>
        <div class="spec-item spec-volume">1fl oz/<br>30ml</div>
      </div>
    </section>
  </main>
</body>
</html>
```